I need a business card design for my new clinic (SPORTS MEDICINE OF KNEE). I am orthopedist, expert in sports surgery, especially knee surgery. I prefer, as colors, the colors of my logo (green, black and white). I already have my logo and should appear on my card. It's good to see my site to have ideas (www.drlucianovarela.com)
It needs contain:
my name: Dr. Luciano Varela
my registration: CRM 584-902
my specialty: Cirurgia do Joelho / Esporte
my address: Centro Executivo - Pinheiral Plaza
Av. Doutor Augusto Brandão Cunha, 2740 sala 0836
Jd. Ipanema - Ribeirão Preto - SP
my phone number: Tel (16) 8245-3908
my clinic phone: (16) 3670-4851
my e-mail: drlucianovarela@mailbox-exemplo.com
my site: www.drlucianovarela.com

Target Market(s)

futures patients

Industry/Entity Type

Clinic

Requirements
Nice to have
• letters not overfilled
straight lines, with few curves

```html
<!DOCTYPE html>
<html lang="pt-BR">
<head>
<meta charset="utf-8">
<title>Varela Traumatologia Esportiva – Cartão de Visita</title>
<link rel="stylesheet" href="https://fonts.googleapis.com/css2?family=Old+Standard+TT:wght@400&display=swap">
<style>
  :root {
    --ink: #1c1c1c;
    --green: #3fae6a;
    --square: #1f2a22;
    --bg-grey: #e6e6e6;
    --bg-white: #fbfbfb;
    --bg-tint: #e4f1e8;
  }
  * { margin: 0; padding: 0; box-sizing: border-box; }
  html, body {
    width: 1200px;
    height: 900px;
    overflow: hidden;
  }
  body {
    font-family: "Old Standard TT", "Times New Roman", serif;
    color: var(--ink);
  }
  .card {
    position: relative;
    width: 1200px;
    height: 900px;
    background: var(--bg-white);
    overflow: hidden;
  }
  .backdrop {
    position: absolute;
    inset: 0;
    background:
      linear-gradient(118deg,
        var(--bg-grey) 0%,
        var(--bg-grey) 14%,
        var(--bg-white) 24%,
        var(--bg-tint) 32%,
        var(--bg-white) 41%,
        var(--bg-white) 52%,
        var(--bg-tint) 60%,
        var(--bg-white) 70%,
        var(--bg-grey) 84%,
        var(--bg-grey) 100%);
  }
  .backdrop-corner {
    position: absolute;
    inset: 0;
    background: linear-gradient(200deg, var(--bg-grey) 0%, rgba(230,230,230,0) 28%);
  }
  .brand {
    position: absolute;
    left: 38px;
    top: 42px;
    display: flex;
    align-items: flex-start;
  }
  .brand-square {
    width: 158px;
    height: 130px;
    background: var(--square);
    border-radius: 12px;
    flex: none;
  }
  .brand-text {
    margin-left: 34px;
  }
  .brand-name {
    font-size: 98px;
    line-height: 1;
    letter-spacing: 3px;
    color: var(--ink);
    margin-top: 0;
  }
  .brand-tagline {
    font-size: 27px;
    letter-spacing: 3px;
    color: var(--green);
    margin-top: -2px;
    margin-left: 12px;
  }
  .contact {
    position: absolute;
    right: 70px;
    top: 376px;
    text-align: right;
    font-size: 30px;
    line-height: 41px;
  }
  .contact .doctor-name {
    margin-bottom: 41px;
  }
</style>
</head>
<body>
  <main class="card">
    <div class="backdrop" role="img" aria-label="Soft grey, white and pale green background tones"></div>
    <div class="backdrop-corner"></div>

    <header class="brand">
      <div class="brand-square"></div>
      <div class="brand-text">
        <div class="brand-name">VARELA</div>
        <div class="brand-tagline">Traumatologia Esportiva</div>
      </div>
    </header>

    <section class="contact">
      <p class="doctor-name">Dr. Luciano Varela</p>
      <p>CRM 584-902</p>
      <p>Cirurgia do Joelho / Esporte</p>
      <p>Centro Executivo - Pinheiral Plaza</p>
      <p>Av. Doutor Augusto Brandão Cunha, 2740 sala 0836</p>
      <p>Jd. Ipanema - Ribeirão Preto - SP</p>
      <p>Tel (16) 8245-3908</p>
      <p>Phone - Clinic: (16) 3670-4851</p>
      <p>drlucianovarela@mailbox-exemplo.com</p>
      <p>www.drlucianovarela.com</p>
    </section>
  </main>
</body>
</html>
```